Book Cover for Christian Book titled, "Climbing Past the Silver Hills"

Size of book cover will be 6" x 9".
The book is about how a person can know beyond a shadow of a doubt that they will go to heaven when they die.
The Title is "Climbing Past the Silver Hills"
Subtitle is "Finding Lasting Peace Through Daily Quiet Prayer and Reflection."
The front of the book should have title, subtitle, and author. The back of the book and spine should have no text and be a solid color.
The uploaded pic is a possibility for a design; but I'm open to other designs.
Whatever images are used need to be very high quality to meet Marrowind Folio Services guidelines. Also, the finished product needs to be sized to match the MFS guide for a 6x9 book.

```html
<!DOCTYPE html>
<html lang="en">
<head>
<meta charset="utf-8">
<title>Climbing Past the Silver Hills – Front Cover</title>
<link rel="stylesheet" href="https://fonts.googleapis.com/css2?family=Anton&family=Oswald:wght@200;600&display=swap">
<style>
  :root {
    --page-bg: #0a72bd;
    --night-indigo: #2b2766;
    --deep-blue: #3d4fb8;
    --sky-blue: #6f8fe6;
    --haze-lavender: #d9dcf6;
    --mist-white: #f4f6fc;
    --path-gold: #f3b54a;
    --path-amber: #ef9a3c;
    --title-white: #ffffff;
    --subtitle-navy: #362d78;
    --author-ink: #1a1a2a;
  }
  * { margin: 0; padding: 0; box-sizing: border-box; }
  html, body {
    width: 1200px;
    height: 960px;
    overflow: hidden;
    background: var(--page-bg);
  }
  .cover {
    position: absolute;
    left: 310px;
    top: 45px;
    width: 580px;
    height: 870px;
    overflow: hidden;
    box-shadow: 0 18px 40px rgba(0, 0, 0, 0.25);
  }
  .cover-art {
    position: absolute;
    inset: 0;
    background:
      radial-gradient(ellipse 34% 48% at 66% 80%, var(--path-gold) 0%, var(--path-amber) 45%, rgba(239,154,60,0) 100%),
      radial-gradient(ellipse 60% 30% at 62% 48%, rgba(244,246,252,0.95) 0%, rgba(244,246,252,0) 100%),
      linear-gradient(180deg,
        var(--night-indigo) 0%,
        var(--deep-blue) 22%,
        var(--sky-blue) 38%,
        var(--haze-lavender) 52%,
        var(--mist-white) 66%,
        #e4ecfb 82%,
        #bfd8f6 100%);
  }
  .title {
    position: absolute;
    left: 52px;
    top: 78px;
    font-family: "Anton", sans-serif;
    color: var(--title-white);
    text-transform: uppercase;
    line-height: 0.92;
    text-shadow: 0 3px 8px rgba(20, 20, 60, 0.45);
  }
  .title-line { display: block; }
  .title-line--small { font-size: 70px; letter-spacing: 0.5px; }
  .title-line--large { font-size: 100px; }
  .title-line--final { font-size: 112px; }
  .subtitle {
    position: absolute;
    left: 38px;
    top: 430px;
    width: 270px;
    padding: 12px 14px 14px;
    background: rgba(244, 246, 252, 0.55);
    font-family: "Oswald", sans-serif;
    font-weight: 600;
    font-size: 29px;
    line-height: 1.08;
    text-transform: uppercase;
    color: var(--subtitle-navy);
  }
  .author {
    position: absolute;
    right: 50px;
    bottom: 48px;
    font-family: "Oswald", sans-serif;
    font-weight: 200;
    font-size: 44px;
    letter-spacing: 0.5px;
    text-transform: uppercase;
    color: var(--author-ink);
  }
</style>
</head>
<body>
  <main class="cover">
    <div class="cover-art" role="img" aria-label="Dreamlike starry sky over misty water, an open door standing in the light, and a golden path with a small figure walking toward it"></div>
    <h1 class="title">
      <span class="title-line title-line--small">Climbing Past</span>
      <span class="title-line title-line--large">The Silver</span>
      <span class="title-line title-line--final">Hills</span>
    </h1>
    <p class="subtitle">Finding Lasting Peace Through Daily Quiet Prayer and Reflection.</p>
    <p class="author">Author's Name</p>
  </main>
</body>
</html>
```